New Business Card Design Project

I need a clean, professional business card. I'd like it to have some color, but not be wild. We do technology consulting and we have clients large and small who trust us with some of their most important data and projects. Simple but not boring should drive all design proposals. Multicolored and two sided, but with a matte finish, I think.
For more on tone, check out our website: http://quorvantis.example

Target Market(s)

Upper management of respected businesses. Tech savvy, but not "hipster".

Industry/Entity Type

Business

Requirements
Must have
• Files need to be provided in .eps and in .pdf in a manner that allows for easy updates.
Must have Name, Title, Phone, Email, Twitter, Website
Nice to have
• Logo/Name shouldn't be too big. One thing I've read several places is that the bigger the logo, the smaller the brand. A good article on dos and don'ts here: http://www.brindlepost.example/2011/02/business-card-experience.html

```html
<!DOCTYPE html>
<html lang="en">
<head>
<meta charset="utf-8">
<title>Quorvantis — Business Card</title>
<link rel="stylesheet" href="https://fonts.googleapis.com/css2?family=Didact+Gothic&family=Pathway+Gothic+One&display=swap">
<style>
  :root {
    --backdrop: #b4b1a4;
    --card-front: #858585;
    --card-back-center: #ffffff;
    --card-back-edge: #e6eaea;
    --ink: #7c7c7c;
    --ink-soft: #8c8c8c;
    --accent-green: #7ba33e;
    --accent-teal: #3a8e9c;
    --white: #ffffff;
  }
  * { margin: 0; padding: 0; box-sizing: border-box; }
  html, body {
    width: 1200px; height: 900px; overflow: hidden;
    background: var(--backdrop);
  }
  .canvas { position: relative; width: 1200px; height: 900px; }

  .card { position: absolute; width: 675px; height: 390px; }

  .card-front {
    left: 40px; top: 100px;
    background: var(--card-front);
  }
  .brand {
    position: absolute; left: 232px; top: 252px;
    display: flex; align-items: center; gap: 16px;
  }
  .brand-dot {
    width: 26px; height: 26px; border-radius: 50%;
    background: var(--accent-teal);
  }
  .brand-name {
    font-family: "Didact Gothic", sans-serif;
    font-size: 36px; letter-spacing: 1px;
    color: var(--white); line-height: 1;
  }

  .card-back {
    left: 428px; top: 415px;
    background: radial-gradient(ellipse at 55% 45%, var(--card-back-center) 35%, var(--card-back-edge) 100%);
  }
  .identity { position: absolute; left: 245px; top: 112px; }
  .person-name {
    font-family: "Pathway Gothic One", sans-serif;
    font-size: 37px; letter-spacing: 2.5px;
    color: var(--ink); line-height: 1;
  }
  .name-rule {
    width: 203px; height: 4px; margin-top: 2px;
    background: var(--accent-green);
  }
  .person-title {
    font-family: "Pathway Gothic One", sans-serif;
    font-size: 26px; letter-spacing: 1.5px;
    color: var(--ink); line-height: 1; margin-top: 6px;
  }

  .contact-list {
    position: absolute; left: 31px; top: 286px;
    list-style: none;
  }
  .contact-item, .contact-phone {
    display: flex; align-items: center; gap: 10px;
    font-family: "Didact Gothic", sans-serif;
    font-size: 17px; color: var(--ink-soft);
    height: 25.5px;
  }
  .contact-item svg, .contact-phone svg { width: 20px; height: 20px; flex: none; }
  .contact-phone { position: absolute; left: 366px; top: 336px; }
</style>
</head>
<body>
<main class="canvas">

  <section class="card card-front" aria-label="Card front">
    <div class="brand">
      <span class="brand-dot" aria-hidden="true"></span>
      <span class="brand-name">QUORVANTIS</span>
    </div>
  </section>

  <section class="card card-back" aria-label="Card back">
    <div class="identity">
      <p class="person-name">DANA WHITLOCK</p>
      <div class="name-rule"></div>
      <p class="person-title">CEO</p>
    </div>

    <ul class="contact-list">
      <li class="contact-item">
        <svg viewBox="0 0 20 20" aria-hidden="true"><circle cx="10" cy="10" r="7" fill="var(--accent-teal)"/></svg>
        <span>quorvantist</span>
      </li>
      <li class="contact-item">
        <svg viewBox="0 0 20 20" aria-hidden="true">
          <circle cx="10" cy="10" r="8" fill="none" stroke="var(--ink)" stroke-width="1.6"/>
          <ellipse cx="10" cy="10" rx="3.5" ry="8" fill="none" stroke="var(--ink)" stroke-width="1.3"/>
          <line x1="2" y1="10" x2="18" y2="10" stroke="var(--ink)" stroke-width="1.3"/>
        </svg>
        <span>www.quorvantis.example</span>
      </li>
      <li class="contact-item">
        <svg viewBox="0 0 20 20" aria-hidden="true">
          <rect x="1" y="4" width="18" height="12" fill="var(--accent-green)"/>
          <polyline points="1,4 10,11 19,4" fill="none" stroke="var(--white)" stroke-width="1.4"/>
        </svg>
        <span>dana@quorvantis.example</span>
      </li>
    </ul>

    <p class="contact-phone">
      <svg viewBox="0 0 20 20" aria-hidden="true">
        <rect x="4" y="1" width="12" height="18" rx="2" fill="var(--ink)"/>
        <rect x="6" y="3.5" width="8" height="11" fill="var(--white)"/>
        <circle cx="10" cy="16.8" r="1" fill="var(--white)"/>
      </svg>
      <span>1-800-555-0142, ext. 700</span>
    </p>
  </section>

</main>
</body>
</html>
```